Simple Logo Design for Semi-Clear Plastic Frosted Card stock

Create a business card on frosted plastic. compliment existing logo elements with a tree trunk, roots, or seed at the lower half and the full logo both on the front.

Contact information will go on a solid portion of the back of this design since this card stock is semi-transparent.

It is important to consider this plastic card stock medium in your design. I found helpful tips and guides listed at velnacard.example: be careful to understand ink printed on plastic cards cannot have too much of a consistent print area or risks peeling and fine lines can easily scratch off.
Updates

2" x 3.5" 20PT Clear Plastic Business cards with Round corners Please get info or templates here: https://www.velnacard.example/product-detail/2-x-35-20pt-clear-plastic-business-cards-with-round-corners

Target Market(s)

Not for profit- religion

Industry/Entity Type

Business

Contact Information for Business Card

Must include complementary elements to the existing logo

Font styles to use
Decorative

Colors
000000

Requirements
Must have
• Elements of community, nature and oneness. Such as: seed, roots, tree trunk, etc.
• Three lines of space on the back for Name, Title, Phone Number.
Nice to have
• I like a light use of decorative elements
Should not have
• No eyes, from faces or animals.

```html
<!DOCTYPE html>
<html lang="en">
<head>
<meta charset="utf-8">
<title>Steadfast Grove — Frosted Business Card</title>
<link rel="stylesheet" href="https://fonts.googleapis.com/css2?family=Josefin+Sans:wght@300;400;600&display=swap">
<style>
  :root {
    --backdrop: #3b3639;
    --frost: #d6d8d9;
    --frost-edge: #eef0f0;
    --frost-pale: #cfd3d3;
    --teal: #35a6a3;
    --teal-deep: #2b8f8c;
    --teal-soft: #6fbdb9;
    --leaf: #67bd46;
    --leaf-soft: #a9d9a3;
    --ink-grey: #858a8c;
  }
  * { margin: 0; padding: 0; box-sizing: border-box; }
  html, body { width: 1200px; height: 1023px; overflow: hidden; }
  body {
    background: var(--backdrop);
    font-family: "Josefin Sans", "Century Gothic", sans-serif;
    position: relative;
  }
  .card {
    position: absolute;
    left: 250px;
    width: 700px;
    height: 400px;
    border-radius: 34px;
    background: linear-gradient(160deg, var(--frost-edge), var(--frost) 55%, var(--frost-pale));
    overflow: hidden;
    box-shadow: 0 18px 40px rgba(0,0,0,0.35);
  }
  .card--front { top: 60px; }
  .card--back { top: 523px; }

  .leaf-scatter {
    position: absolute; left: 0; top: 0; width: 700px; height: 400px;
    background: linear-gradient(200deg, rgba(103,189,70,0.22) 0%, rgba(103,189,70,0.10) 45%, rgba(103,189,70,0) 75%);
  }
  .card--back .leaf-scatter {
    background: linear-gradient(200deg, rgba(169,217,163,0.35) 0%, rgba(169,217,163,0.15) 45%, rgba(169,217,163,0) 75%);
  }

  .holder { position: absolute; left: 44px; top: 38px; z-index: 2; }
  .holder__name {
    font-size: 22px; font-weight: 300; letter-spacing: 3px; color: var(--ink-grey);
  }
  .holder__title {
    font-size: 12px; font-weight: 400; letter-spacing: 3px; color: var(--ink-grey); margin-top: 6px;
  }
  .brand { position: absolute; left: 44px; top: 128px; z-index: 2; }
  .brand__name {
    font-size: 34px; font-weight: 400; letter-spacing: 2px; color: var(--teal);
  }
  .brand__tagline {
    font-size: 11px; font-weight: 400; letter-spacing: 2.5px; color: var(--ink-grey); margin-top: 6px;
  }
  .phone {
    position: absolute; right: 44px; top: 42px; z-index: 2;
    font-size: 18px; font-weight: 300; letter-spacing: 3px; color: var(--ink-grey);
  }
  .tree-emblem {
    position: absolute; left: 150px; bottom: -170px; z-index: 1;
    width: 400px; height: 400px; border-radius: 50%;
    background: radial-gradient(circle at 50% 70%, var(--teal) 0 46%, var(--leaf) 47% 70%, rgba(103,189,70,0) 71%);
  }

  .card--back .holder__name,
  .card--back .holder__title { color: var(--teal-soft); }
  .card--back .brand__name { color: var(--teal-deep); }
  .card--back .tree-emblem {
    background: radial-gradient(circle at 50% 70%, #cfe9ea 0 46%, var(--leaf-soft) 47% 70%, rgba(169,217,163,0) 71%);
  }
</style>
</head>
<body>
  <section class="card card--front">
    <div class="leaf-scatter" role="img" aria-label="Scattered falling green leaves"></div>
    <div class="holder">
      <p class="holder__name">ELIAS MARROW</p>
      <p class="holder__title">DIRECTOR</p>
    </div>
    <p class="phone">012 555 0142</p>
    <div class="brand">
      <p class="brand__name">STEADFAST GROVE</p>
      <p class="brand__tagline">KNOWLEDGE, FRIENDSHIP &amp; PEACE</p>
    </div>
    <div class="tree-emblem" role="img" aria-label="Tree with leafy green crown and teal trunk and roots in a half circle"></div>
  </section>

  <section class="card card--back">
    <div class="leaf-scatter" role="img" aria-label="Scattered pale green falling leaves"></div>
    <div class="holder">
      <p class="holder__name">ELIAS MARROW</p>
      <p class="holder__title">DIRECTOR</p>
    </div>
    <p class="phone">012 555 0142</p>
    <div class="brand">
      <p class="brand__name">STEADFAST GROVE</p>
      <p class="brand__tagline">KNOWLEDGE, FRIENDSHIP &amp; PEACE</p>
    </div>
    <div class="tree-emblem" role="img" aria-label="Pale tree with leafy crown and roots in a half circle"></div>
  </section>
</body>
</html>
```